Packaging design for Hamper boxes

We need to revamp our gift box packaging for our Hamper business. Our business Velvet Baskets (www.velvetbaskets-example.com.au) is a website that curates, packages and delivers hampers for both consumers and corporates. We do everything from champagne and gourmet treats to pamper hampers, baby hampers and beer hampers. Our typical market is 35 - 65 years who are primarily women buying gift hampers for birthdays, thankyous, celebrations, births, sympathy, isolation/care hampers or just to say ' I'm thinking of you'.

We have recently purchased the business so it is going through a bit of a transformation and we want our packaging to be cost effective as we get 1000s of each type of hamper box produced each year. The design will need to be adapted across our box range.

Hampers are a luxury gift and are seen as being special and are designed to make the recipient go ''wow'' and our packaging needs to reflect this.

I will attach the specifics of the box in terms of measurements, must haves, design specifics and brand colours etc.

Target Market(s)

Our typical market is 35 - 65 years who are primarily women buying gift hampers for birthdays, thankyous, celebrations, births, sympathy, isolation/care hampers or just to say ' I'm thinking of you'. Hampers are not a cheap gift so the people who buy hampers have higher disposable income

Font styles to use
Sans Serif
Script
Other font styles liked:
• Rylan regular for logo

Requirements
Must have
• - The hamper box MUST exude quality and a WOW factor
- Colours and logos are listed in the attached brief.
- Box in a dark grey colour (not black).
- Colour grey can vary to that detailed in brief
- Fixed ribbon (orange colour) to front of box design with our logo on ribbon (photo ref 1)
- The word ‘’Happiness’’ to be printed in a script typeface across the front of the box as per photo ref 2. Feel free to choose a different typeface, I don’t particularly like this one on the reference.
- Wording inside the box lid " Enjoy this box full of happiness"
- Please do a version that has a design treatment on the front as well the plain grey with 'Happiness' on it

```html
<!DOCTYPE html>
<html lang="en">
<head>
<meta charset="utf-8">
<title>Velvet Baskets – Hamper Box Dieline</title>
<link rel="stylesheet" href="https://fonts.googleapis.com/css2?family=Great+Vibes&family=Open+Sans:wght@400;600&display=swap">
<style>
  :root {
    --page: #ffffff;
    --board: #2c2c2c;
    --band: #303030;
    --fold: #6b6b6b;
    --crease: #9a9a9a;
    --ribbon: #e8922f;
    --gold: #b08a4a;
    --slot: #ffffff;
    --label: #111111;
    --ink-light: #ffffff;
  }
  html, body {
    margin: 0;
    padding: 0;
    width: 1200px;
    height: 735px;
    overflow: hidden;
    background: var(--page);
  }
  .dieline-sheet { display: block; width: 1200px; height: 735px; }
  .panel-label { font-family: "Open Sans", sans-serif; font-size: 14px; fill: var(--label); }
  .board { fill: var(--board); }
  .fold-line { stroke: var(--fold); stroke-width: 0.8; stroke-dasharray: 4 3; fill: none; }
  .crease-line { stroke: var(--crease); stroke-width: 0.8; fill: none; }
  .front-band { fill: var(--band); }
  .band-edge { stroke: var(--gold); stroke-width: 1; }
  .lid-pattern { fill: #303030; }
  .ribbon { fill: var(--ribbon); }
  .ribbon-slot { stroke: var(--slot); stroke-width: 3.5; stroke-linecap: round; }
  .script-title { font-family: "Great Vibes", cursive; fill: var(--ribbon); }
  .brand-name { font-family: "Open Sans", sans-serif; font-weight: 600; fill: var(--ink-light); letter-spacing: 0.5px; }
  .brand-by { font-family: "Great Vibes", cursive; fill: var(--ink-light); }
</style>
</head>
<body>
<svg class="dieline-sheet" viewBox="0 0 1200 735" xmlns="http://www.w3.org/2000/svg">

  <!-- Outside face -->
  <g class="outside-face">
    <text class="panel-label" x="41" y="23">outside</text>
    <rect class="board" x="40.5" y="36" width="504" height="403"/>
    <rect class="board" x="142" y="439" width="301" height="251"/>

    <line class="fold-line" x1="142" y1="36" x2="142" y2="439"/>
    <line class="fold-line" x1="443" y1="36" x2="443" y2="439"/>
    <line class="fold-line" x1="40.5" y1="137" x2="544.5" y2="137"/>
    <line class="fold-line" x1="40.5" y1="338" x2="544.5" y2="338"/>
    <line class="fold-line" x1="142" y1="439" x2="443" y2="439"/>
    <line class="fold-line" x1="142" y1="640" x2="443" y2="640"/>

    <rect class="front-band" x="229" y="439" width="127" height="251" role="img" aria-label="Faint honeycomb pattern on the front band"/>
    <line class="band-edge" x1="229" y1="439" x2="229" y2="690"/>
    <line class="band-edge" x1="356" y1="439" x2="356" y2="690"/>

    <line class="ribbon-slot" x1="266" y1="103" x2="319" y2="103"/>
    <polygon class="ribbon" points="280,101 307,101 307,195 293.5,183 280,195"/>

    <text class="script-title" x="292" y="547" font-size="40" text-anchor="middle">Happiness</text>
    <text class="brand-name" x="293" y="590" font-size="11" text-anchor="middle">Velvet Baskets</text>

    <line class="ribbon-slot" x1="270" y1="680" x2="322" y2="680"/>
    <polygon class="ribbon" points="283,678 310,678 310,703 296.5,694 283,703"/>
  </g>

  <!-- Inside face -->
  <g class="inside-face">
    <text class="panel-label" x="663" y="31">inside</text>
    <rect class="board" x="662" y="45" width="503" height="402"/>
    <rect class="board" x="763" y="447" width="302" height="252"/>

    <rect class="lid-pattern" x="763" y="146" width="302" height="200" role="img" aria-label="Faint honeycomb pattern inside the lid"/>

    <line class="fold-line" x1="763" y1="45" x2="763" y2="447"/>
    <line class="crease-line" x1="1065" y1="45" x2="1065" y2="146"/>
    <line class="fold-line" x1="1065" y1="146" x2="1065" y2="447"/>
    <line class="fold-line" x1="662" y1="146" x2="1165" y2="146"/>
    <line class="crease-line" x1="662" y1="346" x2="1165" y2="346"/>
    <line class="fold-line" x1="763" y1="447" x2="1065" y2="447"/>
    <line class="fold-line" x1="763" y1="649" x2="1065" y2="649"/>

    <rect class="front-band" x="850" y="447" width="128" height="252" role="img" aria-label="Faint honeycomb pattern on the inner flap band"/>
    <line class="band-edge" x1="850" y1="447" x2="850" y2="699"/>
    <line class="band-edge" x1="978" y1="447" x2="978" y2="699"/>

    <line class="ribbon-slot" x1="893" y1="103" x2="945" y2="103"/>
    <polygon class="ribbon" points="905,100 933,100 933,194 919,182 905,194"/>

    <g class="inner-message" transform="rotate(180 914 548)">
      <text class="script-title" x="914" y="527" font-size="34" text-anchor="middle">A box of happiness</text>
      <text class="brand-by" x="914" y="547" font-size="13" text-anchor="middle">by</text>
      <text class="brand-name" x="914" y="565" font-size="10" text-anchor="middle">Velvet Baskets</text>
    </g>

    <line class="ribbon-slot" x1="887" y1="688" x2="940" y2="688"/>
  </g>
</svg>
</body>
</html>
```